You can visit www.tidecrestvitara.com
for your reference.
What we do :
Not just a nutrition plan, not just workout plan
Its a way of life
Balance between eating the right ingredients for your body, knowing what to avoid, taking care of the body (from skin care to muscle care (heart, lungs, organs...) to mental care)

Target Market(s)

Male and Female

Industry/Entity Type

Health And Wellness

Font styles to use
Script

Colors

Designer to choose colors to be used in the design.

Requirements
Must have
• Must focus of Longevity
Nice to have
• Include picture of Yasmeen in her description.
• You should get inspired from the concept of who we are and what we do for them to reflect this visually in the flyer
• What we do :
• Not just a nutrition plan, not just workout plan
• Its a way of life
• Balance between eating the right ingredients for your body, knowing what to avoid, taking care of the body (from skin care to muscle care (heart, lungs, organs...) to mental care)
Should not have
• Don't include the name Tidecrest Vitara and the Logo as well as the website just put VITARA. kindly use the pictures on the website and the girl doesn’t need to be blonde pick more Brunette, Arabic since we are promoting Dubai. Thank you

```html
<!DOCTYPE html>
<html lang="en">
<head>
<meta charset="utf-8">
<title>VITARA – The Science of Longevity</title>
<link href="https://fonts.googleapis.com/css2?family=Crimson+Text:wght@400&family=Open+Sans:ital,wght@0,300;0,400;1,400&family=Roboto+Condensed:wght@400&family=Great+Vibes&display=swap" rel="stylesheet">
<style>
  :root{
    --bg:#e8e8e6;
    --paper:#ffffff;
    --green:#8dc63f;
    --green-soft:#9ccc55;
    --green-deep:#5f8f22;
    --olive:#4a6520;
    --tan:#c3b69c;
    --rule:#c9b99a;
    --ink:#3b3b3b;
    --brown:#5b4a3a;
    --brown-soft:#8a6a4f;
    --white:#ffffff;
  }
  *{box-sizing:border-box;margin:0;padding:0}
  h1,h2{font-weight:400}
  html,body{width:1200px;height:743px;overflow:hidden;background:var(--bg)}
  .canvas{position:relative;width:1200px;height:743px}
  .flyer{position:absolute;top:54px;width:490px;height:634px;background:var(--paper);overflow:hidden;box-shadow:2px 4px 10px rgba(0,0,0,.25)}
  .flyer--event{left:76px}
  .flyer--coach{left:622px}
  .shapes{position:absolute;inset:0;width:490px;height:634px}
  .photo{position:absolute}
  .abs{position:absolute}

  /* event flyer */
  .hero-photo{left:0;top:0;width:490px;height:420px;
    background:linear-gradient(90deg,#ffffff 0%,#f4f6f2 30%,#dfe5d9 48%,#b7c3ab 62%,#e8ecea 74%,#9fb286 88%,#6f8f46 100%)}
  .brand-title{left:14px;top:56px;font-family:"Crimson Text",serif;font-size:33px;color:#4b4540;letter-spacing:.5px;line-height:1}
  .event-sub{left:16px;top:97px;font-family:"Open Sans",sans-serif;font-weight:300;font-size:16px;color:#222;letter-spacing:.3px}
  .event-date{left:16px;top:121px;font-family:"Crimson Text",serif;font-size:14.5px;color:#555}
  .event-rule{left:16px;top:146px;width:122px;height:3px;background:var(--rule)}
  .questions{left:16px;top:168px;width:290px;list-style:none;font-family:"Open Sans",sans-serif;font-size:11.3px;line-height:13.6px;color:#333}
  .questions li{position:relative;padding-left:17px;margin-bottom:9px}
  .questions svg{position:absolute;left:0;top:2px}
  .food-photo{border-radius:50%;border:3px solid var(--white);box-shadow:0 1px 3px rgba(0,0,0,.2)}
  .food-photo--one{left:16px;top:282px;width:98px;height:98px;background:radial-gradient(circle at 50% 45%,#f4f4f0 0 30%,#3d6b2a 55%,#8d2e25 80%,#2e3a22 100%)}
  .food-photo--two{left:122px;top:306px;width:90px;height:90px;background:radial-gradient(circle at 50% 50%,#f2f4ef 0 25%,#8fb86a 55%,#dfe6d8 100%)}
  .section-head{left:14px;top:402px;font-family:"Open Sans",sans-serif;font-size:13px;line-height:18px;color:#333}
  .benefits{left:16px;top:446px;list-style:none;font-family:"Open Sans",sans-serif;font-size:10.3px;line-height:15.3px;color:#333}
  .benefits li,.coach-list li{position:relative;padding-left:15px}
  .benefits svg,.coach-list svg{position:absolute;left:0;top:3px}
  .services-head{left:308px;top:406px;font-family:"Open Sans",sans-serif;font-size:18px;color:var(--white);letter-spacing:.3px}
  .services{left:308px;top:432px;list-style:none}
  .service{display:flex;align-items:center;height:37.7px}
  .service-icon{width:34px;height:34px;flex:none}
  .service-name{margin-left:8px;font-family:"Open Sans",sans-serif;font-size:10.5px;line-height:11.5px;color:var(--olive);text-transform:uppercase}
  .tagline{font-family:"Great Vibes",cursive;font-size:16px;line-height:21px;color:var(--white)}
  .tagline--left{left:9px;top:585px}

  /* coach flyer */
  .portrait-photo{left:250px;top:0;width:240px;height:300px;
    background:linear-gradient(90deg,#ffffff 0%,#f1ebe3 22%,#e6d3c6 45%,#c9a58e 65%,#e8dacb 82%,#d7c49c 100%)}
  .coach-name{left:14px;top:44px;font-family:"Crimson Text",serif;font-size:29px;color:var(--brown);line-height:1}
  .coach-bio{left:15px;top:85px;width:232px;font-family:"Open Sans",sans-serif;font-size:9.7px;line-height:12.8px;color:#222}
  .coach-bio p+p{margin-top:12.8px}
  .coach-head{left:14px;top:338px;font-family:"Roboto Condensed",sans-serif;font-size:12px;line-height:17px;color:var(--brown);text-transform:uppercase}
  .coach-list{left:15px;top:380px;width:255px;list-style:none;font-family:"Open Sans",sans-serif;font-size:9.8px;line-height:11px;color:#333}
  .coach-list li{margin-bottom:9px}
  .coach-note{left:14px;top:580px;width:235px;font-family:"Open Sans",sans-serif;font-style:italic;font-size:8.4px;line-height:11.2px;color:var(--brown-soft)}
  .testimonials{right:14px;top:344px;width:220px;text-align:right;font-family:"Open Sans",sans-serif;font-style:italic;font-size:8.2px;line-height:11.2px;color:var(--white);white-space:nowrap}
  .testimonial+.testimonial{margin-top:18px}
  .quote-mark{font-family:"Crimson Text",serif;font-style:normal;font-size:22px;line-height:0;vertical-align:-7px;margin-right:3px}
  .tagline--right{right:18px;top:585px;text-align:right}
</style>
</head>
<body>
<svg width="0" height="0" style="position:absolute">
  <symbol id="heart" viewBox="0 0 10 9"><path d="M5 9 L0.8 4.6 A2.4 2.4 0 0 1 5 1.4 A2.4 2.4 0 0 1 9.2 4.6 Z" fill="#8dc63f"/></symbol>
  <symbol id="check" viewBox="0 0 12 12"><circle cx="6" cy="6" r="5.2" fill="none" stroke="#555" stroke-width="1"/><path d="M3.6 6.2 L5.4 7.8 L8.4 4.4" fill="none" stroke="#555" stroke-width="1.1"/></symbol>
  <symbol id="ring" viewBox="0 0 34 34"><circle cx="17" cy="17" r="16" fill="#ffffff" opacity=".25"/><circle cx="17" cy="17" r="13" fill="none" stroke="#ffffff" stroke-width="1.5"/></symbol>
</svg>

<main class="canvas">

  <!-- Event flyer -->
  <section class="flyer flyer--event">
    <div class="photo hero-photo" role="img" aria-label="Misty waterfall over green cliffs with a stack of smooth dark stones"></div>
    <svg class="shapes" viewBox="0 0 490 634" aria-hidden="true">
      <path d="M0 340 C 110 420, 320 440, 490 300 L490 634 L0 634 Z" fill="#ffffff"/>
      <path d="M0 290 C 70 360, 190 405, 330 385 C 200 395, 80 360, 0 305 Z" fill="#5f8f22"/>
      <path d="M490 232 C 430 330, 320 390, 190 398 C 280 405, 270 520, 296 634 L490 634 Z" fill="#9ccc55"/>
      <path d="M0 566 C 120 548, 240 565, 300 634 L0 634 Z" fill="#c3b69c"/>
    </svg>

    <h1 class="abs brand-title">VITARA</h1>
    <p class="abs event-sub">THE SCIENCE OF LONGEVITY</p>
    <p class="abs event-date">Dubai, November 8-10, 2019</p>
    <div class="abs event-rule"></div>

    <ul class="abs questions">
      <li><svg width="11" height="11"><use href="#check"/></svg>Are you overwhelmed and exhausted<br>and feel like there’s no time left for YOU?</li>
      <li><svg width="11" height="11"><use href="#check"/></svg>Are you struggling with Chronic Illness, Mood<br>Swings, Bloating, and Hormone Imbalance?</li>
      <li><svg width="11" height="11"><use href="#check"/></svg>Have you gained weight due to stress-eating<br>and ready take it off?</li>
    </ul>

    <div class="abs photo food-photo food-photo--one" role="img" aria-label="Notebook reading eat well live well surrounded by fresh vegetables"></div>
    <div class="abs photo food-photo food-photo--two" role="img" aria-label="Fresh green vegetables, herbs and avocado on a white table"></div>

    <h2 class="abs section-head">RADIATE LONGEVITY AND FEEL<br>THE BEST VERSION OF YOURSELF!</h2>
    <ul class="abs benefits">
      <li><svg width="9" height="8"><use href="#heart"/></svg>Heal your gut</li>
      <li><svg width="9" height="8"><use href="#heart"/></svg>Balance your Hormone</li>
      <li><svg width="9" height="8"><use href="#heart"/></svg>Feel energetic</li>
      <li><svg width="9" height="8"><use href="#heart"/></svg>Look &amp; feel better than ever</li>
      <li><svg width="9" height="8"><use href="#heart"/></svg>Radiate and glow naturally</li>
      <li><svg width="9" height="8"><use href="#heart"/></svg>Improve nutrition through custom meal plans<br>and counseling for pure vitality and longevity</li>
    </ul>

    <h2 class="abs services-head">OUR SERVICES</h2>
    <ul class="abs services">
      <li class="service">
        <svg class="service-icon" viewBox="0 0 34 34"><use href="#ring"/><rect x="12" y="11" width="10" height="12" rx="2" fill="none" stroke="#fff" stroke-width="1.4"/><path d="M14 15 H20" stroke="#fff" stroke-width="1.4"/></svg>
        <span class="service-name">Weight Loss<br>Counseling</span>
      </li>
      <li class="service">
        <svg class="service-icon" viewBox="0 0 34 34"><use href="#ring"/><circle cx="17" cy="17" r="5" fill="#fff"/></svg>
        <span class="service-name">Functional Nutrition<br>Education</span>
      </li>
      <li class="service">
        <svg class="service-icon" viewBox="0 0 34 34"><use href="#ring"/><path d="M11 23 C 11 14, 17 10, 24 10 C 24 18, 19 23, 11 23 Z M11 23 L20 14" fill="#fff" stroke="#9ccc55" stroke-width="1"/></svg>
        <span class="service-name">Food Allergy<br>Management</span>
      </li>
      <li class="service">
        <svg class="service-icon" viewBox="0 0 34 34"><use href="#ring"/><path d="M12 12 H22 M12 16 H22 M12 20 H22 M12 24 H22" stroke="#fff" stroke-width="1.6" stroke-linecap="round"/></svg>
        <span class="service-name">Gut Health</span>
      </li>
      <li class="service">
        <svg class="service-icon" viewBox="0 0 34 34"><use href="#ring"/><circle cx="14" cy="19" r="3.5" fill="none" stroke="#fff" stroke-width="1.4"/><circle cx="20" cy="14" r="3" fill="none" stroke="#fff" stroke-width="1.4"/></svg>
        <span class="service-name">Balancing<br>Hormone</span>
      </li>
    </ul>

    <p class="abs tagline tagline--left">Transform Your Lifestyle<br>By Changing The Way You Live</p>
  </section>

  <!-- Coach flyer -->
  <section class="flyer flyer--coach">
    <div class="photo abs portrait-photo" role="img" aria-label="Portrait of Yasmeen in a soft pink headscarf, eyes closed, hands pressed together in a sunlit field"></div>
    <svg class="shapes" viewBox="0 0 490 634" aria-hidden="true">
      <path d="M0 240 C 110 320, 300 335, 490 236 L490 634 L0 634 Z" fill="#ffffff"/>
      <path d="M0 220 C 90 300, 230 330, 380 318 C 240 340, 80 300, 0 262 Z" fill="#8dc63f"/>
      <path d="M490 196 C 440 280, 380 318, 330 326 C 288 356, 258 420, 254 480 C 252 540, 272 600, 300 634 L490 634 Z" fill="#9ccc55"/>
      <path d="M194 634 C 260 592, 380 570, 490 566 L490 634 Z" fill="#c3b69c"/>
    </svg>

    <h1 class="abs coach-name">Yasmeen Haddad</h1>
    <div class="abs coach-bio">
      <p>Yasmeen Haddad aboard certified, Transformational Wellness and Nutrition Expert, Member of the Guild of Functional Health and of the Global Coaching Alliance (GCA) uses functional medicine, to help you find the answers to the root cause of disease instead of just treating symptoms.</p>
      <p>Individualized health and wellness programs for pure vitality and longevity.<br>Pushing science and health forward.</p>
    </div>

    <h2 class="abs coach-head">Functional nutrition education is<br>one of the keys to a happier, healthier life.</h2>
    <ul class="abs coach-list">
      <li><svg width="9" height="8"><use href="#heart"/></svg>Personalized meal plans especially done according to your genes</li>
      <li><svg width="9" height="8"><use href="#heart"/></svg>Individualized health and wellness programs for pure vitality and longevity.</li>
      <li><svg width="9" height="8"><use href="#heart"/></svg>Achieve your longevity goals and have fun doing it.</li>
      <li><svg width="9" height="8"><use href="#heart"/></svg>Identify food sensitivities</li>
      <li><svg width="9" height="8"><use href="#heart"/></svg>Balance your hormone</li>
      <li><svg width="9" height="8"><use href="#heart"/></svg>Improve nutrition through meal plans</li>
      <li><svg width="9" height="8"><use href="#heart"/></svg>Counseling</li>
      <li><svg width="9" height="8"><use href="#heart"/></svg>Lose weight</li>
    </ul>

    <p class="abs coach-note">Through this course, my purpose is to inspire you and encourage you to be the best version of yourself. Performing up to your full potential and access a greater level of your life.</p>

    <div class="abs testimonials">
      <p class="testimonial"><span class="quote-mark">“</span>I have more confidence!<br>I struggled to lose weight and feel confi-<br>dent for years until I found the Renewal<br>Reset Program which helped guide my<br>lose 19.5 lbs! ” – Lina</p>
      <p class="testimonial"><span class="quote-mark">“</span>My doctors told me that<br>nutrition did not matter, I knew that was<br>wrong. Now I feel amazing and hopeful again!<br>I’ve reversed leaky Gut, ulcerative colitis, pain,<br>fatigue, depression, and anxiety.” –Omar</p>
      <p class="testimonial"><span class="quote-mark">“</span>After struggling with my<br>health for many years, I finally found some<br>answers to my health challenges. Going<br>through the program, I lost 35 pounds,<br>regained my confidence and rekindled my<br>marriage.” – Mariam</p>
    </div>

    <p class="abs tagline tagline--right">Transform Your Lifestyle<br>By Changing The Way You Live</p>
  </section>

</main>
</body>
</html>
```